Alternative Health Practice - Website redesign

With regard to the welcome image, stock photos can't show the faces of other people. And please don't submit a design for a one-page website.
Hello, I am redesigning a website and need some help from a professional.
The old website is here: peter-lindqvist.net (pls note I don't want to reuse the welcome photo from the old site). Much of the written content will remain the same, so note that I also need a page layout/text colour etc that works for text heavy pages: ie www.peter-lindqvist.net/somatic-articles and www.peter-lindqvist.net/client-reviews
My effort at redesigning is underway here: https://pjlindqvist.sitebuildr.net/my-site-7
The original sitebuildr template is this one: https://www.sitebuildr.net/website-template/view/html/2868?originUrl=https%3A%2F%2Fwww.sitebuildr.net%2Fwebsite%2Ftemplates%2Fhtml%2Fhealth-wellness&tpClick=view_button&esi=6305f015-f1b5-4bdd-8dfa-47b7d756bb68
I'm pretty happy with the colour palette. My name Peter Johan Lindqvist is now the "brand" without Rooted Stillness subtitle. Regarding the Welcome section, if you are going to use my photos, it probably needs to be those two that are already there. If you want to put a stock photo there instead, that's fine.
If you want to propose something quite different to my design, I'm happy to receive design files in Photoshop or whatever and then subsequently replicate on Sitebuildr. Up to you.
Target Market(s)
Mostly women, some men ages 28-60.
Coding
Coded - Design and coding required
Number of Pages Required
5+ page
Look and feel
Each slider illustrates characteristics of the customer's brand and the style your logo design should communicate.

```html
<!DOCTYPE html>
<html lang="en">
<head>
<meta charset="utf-8">
<title>Peter Johan Lindqvist</title>
<link href="https://fonts.googleapis.com/css2?family=Open+Sans:wght@400;600;700&family=Poppins:wght@500;600;700&display=swap" rel="stylesheet">
<style>
:root{
  --sage:#e0dfcd;
  --cream:#ede9df;
  --dark:#333333;
  --footer:#3a3a3a;
  --gold:#c9a04a;
  --gold-a:#cfad6a;
  --gold-b:#a9813a;
  --ink:#2f2f2f;
  --muted:#4a4a4a;
  --white:#ffffff;
}
*{box-sizing:border-box;margin:0;padding:0}
html,body{width:1200px;height:3679px;overflow:hidden}
body{position:relative;font-family:"Open Sans",Arial,sans-serif;color:var(--ink);background:var(--cream)}
.abs{position:absolute}
.band{position:absolute;left:0;width:1200px}
.btn-gold{position:absolute;display:flex;align-items:center;justify-content:center;border-radius:8px;background:linear-gradient(180deg,var(--gold-a),var(--gold-b));color:#2c2410;font-size:14px;box-shadow:0 3px 6px rgba(0,0,0,.18)}
.title{font-family:"Open Sans",Arial,sans-serif;font-weight:600;font-size:34px;color:#333;letter-spacing:.5px}
p.body{font-size:14px;line-height:24px;color:var(--muted)}

/* header + hero */
.hero-band{top:0;height:788px;background:var(--sage)}
.brand{position:absolute;left:60px;top:8px;width:170px;text-align:center}
.brand-mark{width:40px;height:40px;border-radius:50%;background:var(--gold-b);margin:0 auto 8px}
.brand-name{font-family:"Poppins",sans-serif;font-weight:600;font-size:17px;letter-spacing:1.5px;color:#3b3b3b;white-space:nowrap}
.nav{position:absolute;top:36px;left:406px;font-size:14px;color:#444}
.nav a{color:#444;text-decoration:none;position:absolute;white-space:nowrap}
.hero-card{position:absolute;left:60px;top:162px;width:1083px;height:499px;background:var(--dark);border-radius:20px}
.hero-title{position:absolute;left:84px;top:196px;font-family:"Poppins",sans-serif;font-weight:600;font-size:43px;line-height:59px;color:var(--white)}
.hero-title span{color:var(--gold)}
.hero-text{position:absolute;left:84px;top:360px;width:530px;font-size:14px;line-height:24px;color:#e8e8e8}
.btn-white{position:absolute;left:84px;top:533px;width:167px;height:49px;background:#fff;border-radius:8px;display:flex;align-items:center;justify-content:center;font-size:14px;color:#333}
.hero-photo{position:absolute;left:633px;top:84px;width:440px;height:654px;border-radius:14px;background:linear-gradient(160deg,#ecebe8 0%,#d9d6d0 55%,#b9ad95 100%)}

/* about */
.about-band{top:788px;height:805px;background:var(--cream)}
.about-photo{position:absolute;left:60px;top:864px;width:442px;height:653px;border-radius:12px;background:linear-gradient(170deg,#7d8a63 0%,#5a6347 45%,#3f4534 100%)}
.about-caption{position:absolute;left:79px;top:1474px;font-family:"Poppins",sans-serif;font-weight:500;font-size:18px;color:#fff}
.about-box{position:absolute;left:426px;top:928px;width:716px;height:525px;background:var(--sage);border-radius:14px}
.stat{position:absolute;top:1238px}
.stat b{display:block;font-family:"Poppins",sans-serif;font-weight:500;font-size:44px;color:#333;line-height:56px}
.stat span{display:block;font-size:18px;color:#333;margin-top:6px}

/* services */
.svc-band{top:1593px;height:665px;background:var(--sage)}
.card{position:absolute;width:325px;height:237px;background:#fff;border-radius:10px}
.card .icon{position:absolute;left:19px;top:20px;width:56px;height:56px;border-radius:10px;background:#d6d3c4}
.card h3{position:absolute;left:95px;top:38px;font-size:18px;font-weight:600;color:#222;white-space:nowrap}
.card p{position:absolute;left:19px;top:100px;width:290px;font-size:14px;line-height:24px;color:#444}
.card a{position:absolute;left:19px;top:185px;font-size:14px;font-weight:600;color:#222;text-decoration:none}
.card.tilt{left:426px;top:1672px;width:330px;height:240px;background:var(--dark);transform:rotate(-5deg)}
.card.tilt h3{color:#fff}
.card.tilt p{color:#ddd}
.card.tilt a{color:#fff}
.card.tilt .icon{background:#555}

/* contact */
.contact-band{top:2258px;height:597px;background:var(--cream)}
.field{position:absolute;height:49px;background:#fff;border:1px solid #dedbd0;border-radius:8px;box-shadow:0 2px 4px rgba(0,0,0,.12);font-size:14px;color:#777;padding:15px 18px}
.info{position:absolute;left:791px;top:2332px;width:350px;height:447px;border-radius:12px;background:linear-gradient(135deg,#6f6f6f 0%,#565656 45%,#3d3d3d 100%);color:#fff}
.info h3{position:absolute;left:31px;top:38px;font-size:26px;font-weight:600;text-decoration:underline;text-underline-offset:6px}
.info .row{position:absolute;left:24px;display:flex;gap:18px;align-items:center}
.info .row b{display:block;font-size:14px;font-weight:600}
.info .row span{display:block;font-size:14px;margin-top:4px}

/* reviews */
.rev-band{top:2855px;height:401px;background:var(--sage)}
.rev{position:absolute;border-radius:8px;box-shadow:0 2px 8px rgba(0,0,0,.14)}
.rev.side{width:258px;height:168px;top:3000px;background:#f3f2ec}
.rev.main{left:426px;top:2966px;width:349px;height:224px;background:#fff}
.avatar{position:absolute;border-radius:50%;background:linear-gradient(160deg,#e8d4c4,#b18b74)}
.rev .q{position:absolute;font-family:Georgia,serif;font-weight:700;color:#666}

/* footer */
.foot{top:3330px;height:349px;background:var(--footer);color:#fff}
.foot-map{position:absolute;left:270px;top:3345px;width:820px;height:320px;border-radius:40%;background:radial-gradient(ellipse at center,rgba(255,255,255,.07),rgba(255,255,255,0) 70%)}
.foot h4{position:absolute;top:3382px;font-size:19px;font-weight:700}
.foot ul{position:absolute;list-style:none;font-size:13px;line-height:37px;top:3414px;color:#e8e8e8}
.social{position:absolute;top:3588px;width:32px;height:32px;border-radius:50%;background:#fff}
</style>
</head>
<body>

<!-- header + hero -->
<section class="band hero-band"></section>
<div class="brand">
  <div class="brand-mark"></div>
  <div class="brand-name">PETER LINDQVIST</div>
</div>
<nav class="nav">
  <a style="left:0;font-weight:600">Home</a>
  <a style="left:74px">About Us</a>
  <a style="left:170px">Reviews</a>
  <a style="left:257px">Service</a>
  <a style="left:338px">Contact</a>
</nav>
<div class="btn-gold" style="left:975px;top:21px;width:166px;height:48px">Contact US</div>

<div class="hero-card"></div>
<h1 class="hero-title">Where Inner Awareness<br>Meets <span>Healing</span></h1>
<p class="hero-text">Ut arcu dictum sem placerat. Quis felis at sit in non vivamus nunc in habitant. Eget et massa et morbi. Sit arcu sodales dictum penatibus enim felis tincidunt quis. Mi nibh dictum neque eget malesuada facilisi dui dui Cursus est et &nbsp;Sit arcu sodales dictum penatibus enim felis tincidunt quis. Mi nibh dictum neque eget malesuada facilisi dui dui Cursus est et</p>
<div class="btn-white">Contact US</div>
<div class="hero-photo" role="img" aria-label="Practitioner giving a seated client a gentle shoulder treatment in a bright studio"></div>

<!-- about -->
<section class="band about-band"></section>
<div class="about-photo" role="img" aria-label="Portrait photo of the practitioner outdoors"></div>
<div class="about-caption">Peter Johan Lindqvist</div>
<div class="about-box"></div>
<h2 class="title abs" style="left:517px;top:952px">ABOUT US</h2>
<p class="body abs" style="left:517px;top:1029px;width:610px">Ut arcu dictum sem placerat. Quis felis at sit in non vivamus nunc in habitant. Eget et massa et morbi. Sit arcu sodales dictum penatibus enim felis tincidunt quis. Mi nibh dictum neque eget malesuada facilisi dui dui Cursus est et &nbsp;Sit arcu sodales dictum penatibus enim felis tincidunt quis.</p>
<p class="body abs" style="left:517px;top:1140px;width:610px">Ut arcu dictum sem placerat. Quis felis at sit in non vivamus nunc in habitant. Eget et massa et morbi. Sit arcu sodales dictum penatibus enim felis tincidunt quis.</p>
<div class="stat" style="left:517px"><b>15+</b><span>Years Expriance</span></div>
<div class="stat" style="left:713px"><b>10</b><span>Best Award</span></div>
<div class="stat" style="left:872px"><b>1k+</b><span>Happy Clients</span></div>
<div class="btn-gold" style="left:517px;top:1376px;width:167px;height:49px">Contact US</div>

<!-- services -->
<section class="band svc-band"></section>
<h2 class="title abs" style="left:60px;top:1674px">CORE SERVICE</h2>
<p class="body abs" style="left:60px;top:1745px;width:345px">Ut arcu dictum sem placerat. Quis felis at sit in non vivamus nunc in habitant. Eget et massa et morbi. Sit arcu sodales</p>
<div class="btn-gold" style="left:60px;top:1846px;width:167px;height:49px">Contact US</div>

<div class="card tilt"><div class="icon" role="img" aria-label="Lightbulb icon"></div><h3>Somatic Awareness</h3><p>Ut arcu dictum sem placerat. Quis felis at sit in non vivamus nunc in habitant. Eget et massa et morbi. Sit arcu sodales</p><a>Read More</a></div>
<div class="card" style="left:816px;top:1661px"><div class="icon" role="img" aria-label="Group of people icon"></div><h3>Trauma-Informed Body</h3><p>Ut arcu dictum sem placerat. Quis felis at sit in non vivamus nunc in habitant. Eget et massa et morbi. Sit arcu sodales</p><a>Read More</a></div>
<div class="card" style="left:60px;top:1958px"><div class="icon" role="img" aria-label="Emotion faces icon"></div><h3>Emotional Integration</h3><p>Ut arcu dictum sem placerat. Quis felis at sit in non vivamus nunc in habitant. Eget et massa et morbi. Sit arcu sodales</p><a>Read More</a></div>
<div class="card" style="left:438px;top:1958px"><div class="icon" role="img" aria-label="Listening icon"></div><h3>Deep Listening Sessions</h3><p>Ut arcu dictum sem placerat. Quis felis at sit in non vivamus nunc in habitant. Eget et massa et morbi. Sit arcu sodales</p><a>Read More</a></div>
<div class="card" style="left:816px;top:1958px"><div class="icon" role="img" aria-label="Inquiry document icon"></div><h3>Guided Self-Inquiry</h3><p>Ut arcu dictum sem placerat. Quis felis at sit in non vivamus nunc in habitant. Eget et massa et morbi. Sit arcu sodales</p><a>Read More</a></div>

<!-- contact -->
<section class="band contact-band"></section>
<h2 class="title abs" style="left:68px;top:2332px">CONTECT US</h2>
<div class="field" style="left:60px;top:2415px;width:380px">Full Name</div>
<div class="field" style="left:456px;top:2415px;width:400px">Address</div>
<div class="field" style="left:60px;top:2494px;width:380px">Email</div>
<div class="field" style="left:456px;top:2494px;width:400px">Phone</div>
<div class="field" style="left:60px;top:2572px;width:796px;height:130px">Message...</div>
<div class="btn-gold" style="left:60px;top:2729px;width:167px;height:49px">Contact US</div>

<div class="info" role="group" aria-label="Contact information">
  <h3>Information</h3>
  <div class="row" style="top:122px">
    <svg width="46" height="46" viewBox="0 0 24 24" fill="#fff"><path d="M6.6 10.8a15.1 15.1 0 0 0 6.6 6.6l2.2-2.2a1 1 0 0 1 1-.25 11.4 11.4 0 0 0 3.6.57 1 1 0 0 1 1 1V20a1 1 0 0 1-1 1A17 17 0 0 1 3 4a1 1 0 0 1 1-1h3.5a1 1 0 0 1 1 1c0 1.25.2 2.45.57 3.57a1 1 0 0 1-.25 1z"/></svg>
    <div><b>Phone</b><span>0400 555 218</span></div>
  </div>
  <div class="row" style="top:228px">
    <svg width="50" height="40" viewBox="0 0 50 36"><rect x="1" y="1" width="48" height="34" rx="3" fill="#fff"/><path d="M2 3 25 20 48 3" fill="none" stroke="#5a5a5a" stroke-width="3"/></svg>
    <div><b>Email</b><span>peter@lindqvist-mail.net</span></div>
  </div>
  <div class="row" style="top:330px;left:36px">
    <svg width="30" height="50" viewBox="0 0 24 36" fill="#fff"><path d="M12 0C5.4 0 0 5.4 0 12c0 9 12 24 12 24s12-15 12-24C24 5.4 18.6 0 12 0zm0 17a5 5 0 1 1 0-10 5 5 0 0 1 0 10z"/></svg>
    <div><b>Address</b><span>Fernvale, Coastland</span></div>
  </div>
</div>

<!-- reviews -->
<section class="band rev-band"></section>
<h2 class="title abs" style="left:0;width:1200px;text-align:center;top:2892px">CLIENT REVIEWS</h2>
<svg class="abs" style="left:90px;top:3074px" width="32" height="26" viewBox="0 0 32 26"><path d="M30 13H4M13 3 3 13l10 10" fill="none" stroke="#444" stroke-width="3.5" stroke-linecap="round"/></svg>
<svg class="abs" style="left:1080px;top:3074px" width="32" height="26" viewBox="0 0 32 26"><path d="M2 13h26M19 3l10 10-10 10" fill="none" stroke="#444" stroke-width="3.5" stroke-linecap="round"/></svg>

<div class="rev side" style="left:153px">
  <div class="avatar" role="img" aria-label="Reviewer avatar" style="left:10px;top:10px;width:50px;height:50px"></div>
  <div class="abs" style="left:68px;top:26px;font-size:14px;color:#444">Marelle</div>
  <div class="q" style="left:6px;top:78px;font-size:22px">&ldquo;</div>
  <div class="abs" style="left:28px;top:84px;width:218px;font-size:10px;line-height:18px;color:#777">Ut arcu dictum sem placerat. Quis felis at sit in non vivamus nunc in habitant. Eget et massa et morbi. Sit arcu sodalesdictum sem placerat. Quis felis at</div>
</div>
<div class="rev main">
  <div class="avatar" role="img" aria-label="Reviewer avatar" style="left:10px;top:12px;width:72px;height:72px"></div>
  <div class="abs" style="left:91px;top:38px;font-size:18px;color:#222">Marelle</div>
  <div class="q" style="left:8px;top:106px;font-size:32px">&ldquo;</div>
  <div class="abs" style="left:40px;top:118px;width:300px;font-size:14px;line-height:24px;color:#444">Ut arcu dictum sem placerat. Quis felis at sit in non vivamus nunc in habitant. Eget et massa et morbi. Sit arcu sodalesdictum sem placerat. Quis felis at &rdquo;</div>
</div>
<div class="rev side" style="left:791px">
  <div class="avatar" role="img" aria-label="Reviewer avatar" style="left:10px;top:10px;width:50px;height:50px"></div>
  <div class="abs" style="left:68px;top:26px;font-size:14px;color:#444">Marelle</div>
  <div class="q" style="left:6px;top:78px;font-size:22px">&ldquo;</div>
  <div class="abs" style="left:28px;top:84px;width:218px;font-size:10px;line-height:18px;color:#777">Ut arcu dictum sem placerat. Quis felis at sit in non vivamus nunc in habitant. Eget et massa et morbi. Sit arcu sodalesdictum sem placerat. Quis felis at</div>
</div>

<!-- footer -->
<footer class="band foot"></footer>
<div class="foot-map" role="img" aria-label="Faint world map backdrop"></div>
<div class="abs" style="left:60px;top:3364px;width:275px;text-align:center;color:#fff">
  <div style="width:56px;height:56px;border-radius:50%;background:#fff;margin:0 auto 10px"></div>
  <div style="font-family:'Poppins',sans-serif;font-weight:600;font-size:28px;line-height:38px;letter-spacing:2px;white-space:nowrap">PETER LINDQVIST</div>
</div>
<p class="abs" style="left:60px;top:3488px;width:370px;font-size:14px;line-height:24px;color:#eee">Ut arcu dictum sem placerat. Quis felis at sit in non vivamus nunc in habitant. Eget et massa et morbi. Sit arcu sodalesdictum sem placerat. Quis felis at</p>
<div class="social" style="left:61px" aria-label="Social link 1"></div>
<div class="social" style="left:132px" aria-label="Social link 2"></div>
<div class="social" style="left:203px" aria-label="Social link 3"></div>
<div class="social" style="left:275px" aria-label="Social link 4"></div>

<div class="foot">
  <h4 style="left:697px">Services</h4>
  <ul style="left:697px"><li>Somatic Awareness</li><li>Trauma-Informed Body</li><li>Emotional Integration</li><li>Deep Listening Sessions</li><li>Guided Self-Inquiry</li></ul>
  <h4 style="left:895px">Use Full Link</h4>
  <ul style="left:895px;font-size:12px;line-height:36px"><li>Home</li><li>About Us</li><li>Service</li><li>Contect Us</li><li>Client Reviews</li></ul>
  <h4 style="left:1051px;top:3386px">Legal</h4>
  <ul style="left:1051px;font-size:12px;line-height:36px"><li>Privacy Policy</li><li>Terms Of Use</li><li>Cookie Policy</li></ul>
</div>
<div class="abs" style="left:60px;top:3640px;width:1081px;height:1px;background:#8a8a8a"></div>
<div class="abs" style="left:0;width:1200px;top:3651px;text-align:center;font-size:13px;color:#ddd">Copyright &copy; 2025 All Right Reserved</div>

</body>
</html>
```